Lantern Image Works

Its a flyer to promote free seminars for alternative photographic techniques. We need to include brief information about the two people who are giving the seminar, Gordon Ashby and Alan Brook and a short description of the methods used. Photo gravure; Gum bichromate, carbon printing. The Seminars are FREE, and will be on march 14th and 15th at Lantern Works Studios, 17 Marlow Road Kingston upon Thames KT4 7QD we would like to add a things saying 'please let us know you are coming on 'lanternimageworks@mailbox.example or via our friendbook page (also called lantern images Works) if we could add a friendbook logo thing
Seminars will be 2 hours long 12 -2 pm

Strap line something like " Discover the creativity of early photographic processes'

And we need the fliers by Saturday!

```html
<!DOCTYPE html>
<html lang="en">
<head>
<meta charset="utf-8">
<title>Lantern Image Works – Early Photographic Processes Seminars</title>
<link rel="stylesheet" href="https://fonts.googleapis.com/css2?family=Archivo:wght@800&family=Lato:wght@400;700&family=Oswald:wght@500&display=swap">
<style>
  :root {
    --backdrop: #2e2e2e;
    --paper-top: #d9d3b9;
    --paper-bottom: #f1f1ef;
    --navy: #1f3d7a;
    --band-blue: #1e4b95;
    --band-deep: #183a78;
    --title-grey: #3b3b3b;
    --panel-grey: #474747;
    --gold: #f4b323;
    --gold-text: #f6b628;
    --white: #ffffff;
    --frame: #e4e4e2;
  }
  * { margin: 0; padding: 0; box-sizing: border-box; }
  html, body { width: 904px; height: 1200px; overflow: hidden; }
  body { background: var(--backdrop); position: relative; font-family: "Lato", sans-serif; }

  .flyer {
    position: absolute; left: 42px; top: 17px;
    width: 692px; height: 983px;
    transform: scale(1.185); transform-origin: top left;
    background: linear-gradient(180deg, var(--paper-top) 0%, #dedbcc 40%, var(--paper-bottom) 75%, var(--white) 100%);
    overflow: hidden;
    box-shadow: 0 6px 18px rgba(0,0,0,.45);
  }

  .headline {
    position: absolute; left: 0; top: 22px; width: 100%;
    text-align: center; font-family: "Archivo", sans-serif; font-weight: 800;
    font-size: 43px; line-height: 60px; color: var(--title-grey); letter-spacing: -0.5px;
  }

  .presenters {
    position: absolute; left: 122px; top: 140px; width: 448px; height: 52px;
    border-radius: 26px; background: var(--navy); border: 3px solid var(--white);
    box-shadow: 0 2px 4px rgba(0,0,0,.35);
    color: var(--white); font-size: 26px; line-height: 46px; text-align: center;
  }

  .print {
    position: absolute; background: var(--frame); padding: 12px;
    box-shadow: 3px 8px 12px rgba(0,0,0,.45);
  }
  .print .plate { width: 100%; height: 100%; }
  .print--dancer { left: 18px; top: 210px; width: 282px; height: 305px; transform: rotate(-7deg); }
  .print--dancer .plate { background: radial-gradient(ellipse at 45% 45%, #7a6a63 0%, #3a2a26 45%, #1c1312 100%); }
  .print--woods { left: 368px; top: 208px; width: 288px; height: 278px; transform: rotate(8deg); }
  .print--woods .plate { background: linear-gradient(180deg, #6f8fa0 0%, #2f4a56 55%, #18262d 100%); }
  .print--portrait { left: 192px; top: 350px; width: 270px; height: 270px; padding: 11px; background: #f4f4f4; transform: none; }
  .print--portrait .plate { background: radial-gradient(circle at 50% 45%, #3b3b3b 0%, #151515 55%, #050505 100%); }
  .print--city { left: 296px; top: 692px; width: 168px; height: 178px; padding: 9px; transform: rotate(7deg); }
  .print--city .plate { background: linear-gradient(180deg, #8a7a52 0%, #6e5e3e 55%, #3f3424 100%); }

  .free-badge { position: absolute; left: 474px; top: 461px; width: 208px; height: 208px; }
  .free-badge text { font-family: "Oswald", sans-serif; font-weight: 500; fill: var(--white); text-anchor: middle; }

  .methods {
    position: absolute; left: 0; top: 635px; width: 517px; height: 45px;
    background: var(--navy); clip-path: polygon(0 0, 97% 0, 100% 100%, 0 100%);
    color: var(--white); font-size: 18.5px; line-height: 45px; padding-left: 20px;
  }

  .when-where {
    position: absolute; left: 0; top: 693px; width: 299px; height: 162px;
    background: var(--panel-grey); border-radius: 0 10px 10px 0; padding: 10px 18px;
    color: var(--white);
  }
  .when-where .date-lead { font-size: 26px; line-height: 32px; }
  .when-where .date-days { font-size: 26px; line-height: 32px; color: var(--gold-text); }
  .when-where .venue { font-size: 18px; line-height: 24px; margin-top: 8px; }
  .when-where .venue strong { color: var(--gold-text); font-weight: 700; }
  .when-where .address { font-size: 16px; line-height: 22px; }

  .session-time {
    position: absolute; left: 472px; top: 750px; width: 220px; height: 120px;
    background: var(--gold); clip-path: polygon(8% 0, 100% 0, 100% 100%, 12% 100%, 0 20%);
    color: var(--navy); text-align: right; padding: 8px 12px 0 0;
  }
  .session-time .label { font-size: 25px; line-height: 32px; }
  .session-time .length { font-size: 20px; line-height: 28px; color: #1e2a44; }
  .session-time .hours { font-size: 27px; line-height: 36px; color: #1e2a44; }

  .contact-band { position: absolute; left: 0; top: 868px; width: 692px; height: 115px; }
  .contact-band .band-shape { position: absolute; left: 0; top: 0; width: 692px; height: 115px; }
  .rsvp {
    position: absolute; left: 16px; top: 12px;
    font-family: "Oswald", sans-serif; font-weight: 500; font-size: 23px; letter-spacing: .3px;
    color: var(--white); text-transform: uppercase;
  }
  .email {
    position: absolute; left: 14px; top: 52px; height: 28px;
    padding-left: 27px; white-space: nowrap;
    color: var(--white); font-size: 20px; line-height: 28px;
  }
  .email .envelope { position: absolute; left: 0; top: 7px; width: 20px; height: 14px; }
  .social { position: absolute; right: 16px; top: 50px; text-align: right; color: var(--white); }
  .social .hint { font-size: 13px; line-height: 18px; }
  .social .handle { font-size: 20px; line-height: 26px; white-space: nowrap; }
  .social .marker { width: 17px; height: 17px; background: var(--white); display: inline-block; vertical-align: -2px; margin-right: 6px; }
</style>
</head>
<body>
  <main class="flyer">
    <h1 class="headline">Discover the creativity of early<br>photographic processes</h1>
    <p class="presenters">By Gordon Ashby and Alan Brook</p>

    <figure class="print print--dancer"><div class="plate" role="img" aria-label="Sepia-toned photograph of a dancer mid-leap in a flowing skirt"></div></figure>
    <figure class="print print--woods"><div class="plate" role="img" aria-label="Blue-toned photograph of bare trees reflected in still water"></div></figure>
    <figure class="print print--portrait"><div class="plate" role="img" aria-label="Black and white portrait photograph of a young person"></div></figure>

    <svg class="free-badge" viewBox="-104 -104 208 208" aria-label="The seminars are free">
      <g fill="#ffffff">
        <rect x="-75" y="-75" width="150" height="150"/>
        <rect x="-75" y="-75" width="150" height="150" transform="rotate(15)"/>
        <rect x="-75" y="-75" width="150" height="150" transform="rotate(30)"/>
        <rect x="-75" y="-75" width="150" height="150" transform="rotate(45)"/>
        <rect x="-75" y="-75" width="150" height="150" transform="rotate(60)"/>
        <rect x="-75" y="-75" width="150" height="150" transform="rotate(75)"/>
        <circle r="93"/>
      </g>
      <g fill="#1f3d7a">
        <rect x="-69" y="-69" width="138" height="138"/>
        <rect x="-69" y="-69" width="138" height="138" transform="rotate(15)"/>
        <rect x="-69" y="-69" width="138" height="138" transform="rotate(30)"/>
        <rect x="-69" y="-69" width="138" height="138" transform="rotate(45)"/>
        <rect x="-69" y="-69" width="138" height="138" transform="rotate(60)"/>
        <rect x="-69" y="-69" width="138" height="138" transform="rotate(75)"/>
        <circle r="87"/>
      </g>
      <text y="-36" font-size="24">THE</text>
      <text y="-5" font-size="22">SEMINARS ARE</text>
      <text y="52" font-size="58">FREE</text>
    </svg>

    <p class="methods">PHOTO GRAVURE:&nbsp; Gum bichromate, carbon printing</p>

    <section class="when-where">
      <p class="date-lead">On march</p>
      <p class="date-days">14th and 15th</p>
      <p class="venue">At: <strong>LANTERN WORKS STUDIOS</strong></p>
      <p class="address">17 Marlow Road Kingston upon<br>Thames KT4 7QD</p>
    </section>

    <figure class="print print--city"><div class="plate" role="img" aria-label="Warm-toned early process print of a misty city skyline"></div></figure>

    <section class="session-time">
      <p class="label">Seminars time:</p>
      <p class="length">2 hours long</p>
      <p class="hours">12 -2 pm</p>
    </section>

    <footer class="contact-band">
      <svg class="band-shape" viewBox="0 0 692 115" preserveAspectRatio="none" aria-hidden="true">
        <defs>
          <linearGradient id="bandFill" x1="0" y1="0" x2="0" y2="1">
            <stop offset="0" stop-color="#1e4b95"/>
            <stop offset="1" stop-color="#183a78"/>
          </linearGradient>
        </defs>
        <polygon points="0,0 390,0 412,22 692,22 692,115 0,115" fill="url(#bandFill)"/>
      </svg>
      <p class="rsvp">Please let us know you are coming on</p>
      <p class="email">
        <svg class="envelope" viewBox="0 0 20 14" aria-hidden="true">
          <rect x="0.5" y="0.5" width="19" height="13" fill="#f4b323" stroke="#f4b323"/>
          <polyline points="1,1 10,8 19,1" fill="none" stroke="#1e4b95" stroke-width="1.5"/>
        </svg>
        <span class="address-text">lanternimageworks@mailbox.example</span>
      </p>
      <div class="social">
        <p class="hint">or via our friendbook page</p>
        <p class="handle"><span class="marker"></span>lantern images Works</p>
      </div>
    </footer>
  </main>
</body>
</html>
```